Web Design - RESPONSIVE Design

People Review Site
We are in the process of building a site that reviews people in different categories (Eg Students, Politicians, actors etc.).
Ideally the design would be similar to http://brightlister.sg.lanternweave.com/ or coolpeek.com

We have the engine ready but the front end needs to be worked on and the deliverables will include HTML, Royalty Free Images and CSS for the responsive design.

Users are able to post anyone's profile (name and category combination being unique) to the site along with their comments (see profile page details below). Other users will be able to comment and will be able to vote (thumbs up and thumbs down) after logging in.
We need a design that will have the following features :
1. Home Page :
The layout should be more Web2.0 type design and should have
Search (Based on category / name / handle)
Add Profile Button -> Should take to login page that will lead to profiles management page
Login (my Account)– See Login Result Page for what happens.
Featured Listing / New / Latest Listings
A small excerpt about us with space for an introduction video
This should also have a placeholder for qv/chirpnet feed.
Bottom should have links for about us type pages - standard text pages

2. Search Results page

The results should be like tackwall – keep scrolling down and get new results.
Result should have the name/handle and the categories the person is in, thumbs up and thumbs down rating (profile voted by other people) and starting 20 words of one of the characteristics of the profile(explained below). Clicking on the result will take the user to Profile Information Page for that individual.
There needs to be a link for creating a new profile.

3. Profile Information Page

Page will have the following information about the person :
Name / Handle
Category
Comments & Supporting Information (that have been entered by the person who has created the profile)
Thumbs-up and Thumbs down count with option to vote
Followup comments by other users
Place for the user to enter his / her comments and rating

When anyone wants to post a comment about a listing, they have to connect using their email or QV account and signup – Then they will be redirected to be able to add the comments.

4. Login Results Page (Profiles Management Page)

• Show all profiles / entries that the user has created. Allow to edit the information about the profiles. Also be able to change own profile – password etc.
• Show all profiles that user has voted on or commented on.
• Link to Add New Profile

5. Add Profile Page :
• Name / Handle
• Category/Categories for this profile
• Supporting information (Pictures)
• Associated website link
• Comment Text Area for detailed review.

Target Market(s)

Typical Internet users interested in reviewing others!

Industry/Entity Type

Number of Pages Required

5+ page

Font styles to use
Serif
Sans Serif

Requirements
Must have
• Web 2.0 type design, Responsive Design
Should not have
• Should not be a pagecrate template!! We are not using a pagecrate template for our design!

```html
<!DOCTYPE html>
<html lang="en">
<head>
<meta charset="utf-8">
<title>Peerscope</title>
<link href="https://fonts.googleapis.com/css2?family=Arimo:wght@400;700&display=swap" rel="stylesheet">
<style>
:root{
  --orange:#f7a51c;
  --ink:#2b2b2b;
  --text:#555;
  --line:#e3e3e3;
  --page:#f1f1f1;
  --card:#ffffff;
  --panel:#2f3133;
  --footer:#3a3a3a;
  --footer-dark:#2c2c2c;
}
*{box-sizing:border-box;margin:0;padding:0}
html,body{width:682px;height:1200px;overflow:hidden}
body{background:var(--page);font-family:"Arimo",Arial,sans-serif;color:var(--text);position:relative}
.abs{position:absolute}
.page{left:42px;top:12px;width:598px;height:1176px;background:var(--card);border-top:2px solid var(--orange);box-shadow:0 0 3px rgba(0,0,0,.08)}
.brand{left:56px;top:34px;display:flex;align-items:center;gap:6px;font-size:15px;font-weight:700;color:var(--ink);letter-spacing:.4px}
.brand .mark{width:10px;height:10px;background:var(--orange)}
.field{border:1px solid #d6d6d6;background:#fff;font-size:5.5px;color:#aaa;padding:0 5px;display:flex;align-items:center}
.btn{background:var(--orange);color:#fff;font-weight:700;display:flex;align-items:center;justify-content:center}
.login{left:570px;top:33px;width:55px;height:17px;font-size:7px}
.nav{left:56px;top:70px;width:570px;height:27px;border-top:1px solid var(--line);border-bottom:1px solid var(--line);display:flex;justify-content:space-between;align-items:center;padding:0 22px;font-size:7px;color:#888;letter-spacing:.3px}
.nav .active{color:var(--orange)}
.nav .sep{color:#aaa}
.hero{left:57px;top:103px;width:569px;height:254px;background:linear-gradient(100deg,#9bb27a 0%,#d9c2a8 30%,#e0b35a 48%,#c9b4a8 62%,#e0783a 80%,#a8c08e 100%)}
.search{left:94px;top:341px;width:496px;height:49px;background:var(--panel);box-shadow:0 14px 14px -8px rgba(0,0,0,.35)}
.search .lbl{color:var(--orange);font-size:7.5px;top:5px}
.search .field{height:20px;top:17px;border-radius:3px;border:none}
.search-btn{left:401px;top:17px;width:85px;height:20px;border-radius:3px;font-size:8.5px;font-weight:400}
.tabs{left:57px;top:417px;width:379px;height:23px;display:flex;border:1px solid var(--line);border-bottom:none}
.tab{flex:1;display:flex;align-items:center;justify-content:center;font-size:7.5px;font-weight:700;color:#777;background:#f7f7f7;border-left:1px solid var(--line)}
.tab.active{background:var(--orange);color:#fff;border-left:none;flex:1.12}
.listings{left:57px;top:440px;width:379px;height:361px;border:1px solid var(--line)}
.listing{position:absolute;left:0;width:377px;height:178px}
.listing .title{left:49px;top:23px;width:217px;font-size:11px;font-weight:400;color:var(--ink);padding-bottom:5px;border-bottom:1px dotted #bbb}
.listing .meta{left:49px;top:45px;font-size:6px;color:#666;display:flex;gap:15px}
.meta a{color:var(--orange);text-decoration:underline}
.listing .photo{left:1px;top:69px;width:146px;height:96px;background:linear-gradient(135deg,#cfe0ef,#b7a08a 45%,#8aa0b8 75%,#dde6ee);border:2px solid #fff;box-shadow:0 0 2px rgba(0,0,0,.3)}
.listing .sub{left:160px;top:73px;font-size:8.5px;font-weight:400;color:var(--ink)}
.listing .stars{left:159px;top:84px;font-size:11px;color:var(--orange);letter-spacing:.5px}
.listing .body{left:160px;top:103px;width:216px;font-size:5.6px;line-height:12.5px;color:#666}
.listing .more{left:160px;top:150px;width:48px;height:17px;font-size:6px;border-radius:2px}
.side-h{font-size:13px;font-weight:700;color:var(--ink);letter-spacing:.3px}
.side-h .accent{color:var(--orange)}
.feed{left:454px;width:172px;height:49px;border-bottom:1px dotted #bbb}
.feed .thumb{left:0;top:0;width:34px;height:30px}
.feed p{position:absolute;left:39px;top:-3px;width:133px;font-size:5.3px;line-height:11px;color:#555}
.hl{color:var(--orange)}
.tweet{left:454px;width:172px;height:50px;border-bottom:1px dotted #bbb;font-size:5.3px;line-height:8.8px;color:#555}
.tweet .when{color:var(--orange);display:block}
.divider{left:57px;top:818px;width:569px;border-top:1px solid var(--line)}
.intro-h{left:57px;top:830px}
.intro p{position:absolute;left:57px;width:333px;font-size:5.6px;line-height:11.2px;color:#888}
.video{left:426px;top:832px;width:200px;height:132px;background:linear-gradient(90deg,#7a1418 0%,#b3242a 40%,#8e1a1e 70%,#1e3a8a 100%)}
.video .bar{left:0;bottom:0;width:200px;height:16px;background:#1b1b1b}
.footer{left:57px;top:990px;width:569px;height:186px;background:var(--footer);border-bottom:2px solid var(--orange)}
.footer h4{position:absolute;top:16px;font-size:9px;font-weight:400;color:var(--orange);letter-spacing:.3px}
.f-links{left:16px;top:36px;font-size:7px;line-height:14px;color:#bbb;list-style:none}
.news{left:109px;width:128px;height:33px;border-bottom:1px solid #4a4a4a;font-size:5.5px;line-height:10px;color:#ccc}
.news b{font-weight:400;color:#eee}
.news .day{position:absolute;left:112px;top:5px;width:16px;height:13px;background:#242424;color:#fff;font-size:5.5px;display:flex;align-items:center;justify-content:center}
.contact{left:273px;top:39px;font-size:5.5px;color:#bbb}
.contact ul{list-style:none;margin-top:9px}
.contact li{line-height:14px;position:relative;padding-left:12px}
.contact li::before{content:"";position:absolute;left:1px;top:5px;width:4px;height:4px;border-radius:50%;background:#bbb}
.f-input{width:128px;height:21px;border:1px solid #666;color:#aaa;font-size:5.5px;display:flex;align-items:center;padding-left:9px}
.submit{left:428px;top:98px;width:60px;height:20px;font-size:8px}
.bottom{left:0;top:152px;width:569px;height:32px;background:var(--footer-dark);font-size:5.5px;color:#bbb}
</style>
</head>
<body>
<div class="abs page"></div>

<header>
  <div class="abs brand"><span class="mark"></span>PEERSCOPE</div>
  <div class="abs field" style="left:346px;top:33px;width:104px;height:17px">Name :</div>
  <div class="abs field" style="left:458px;top:33px;width:104px;height:17px">Email :</div>
  <div class="abs btn login">LOGIN</div>
  <nav class="abs nav">
    <span class="active">HOME</span><span class="sep">/</span><span>ABOUT US</span><span class="sep">/</span><span>FEATURED</span><span class="sep">/</span><span>NEWS</span><span class="sep">/</span><span>REVIEWS</span><span class="sep">/</span><span>CONTACT US</span>
  </nav>
</header>

<section>
  <div class="abs hero" role="img" aria-label="Photo of smiling students holding books and folders on a campus"></div>
  <svg class="abs" style="left:592px;top:200px" width="12" height="50" viewBox="0 0 12 50"><path d="M1 1 L11 25 L1 49" fill="none" stroke="#fff" stroke-width="1.2"/></svg>
  <form class="abs search">
    <span class="abs lbl" style="left:10px">Category</span>
    <span class="abs lbl" style="left:142px">Name</span>
    <span class="abs lbl" style="left:272px">Handle</span>
    <div class="abs field" style="left:8px;width:124px;justify-content:space-between">Select :<svg width="7" height="4"><path d="M0 0h7L3.5 4z" fill="#333"/></svg></div>
    <div class="abs field" style="left:140px;width:123px">Type Here :</div>
    <div class="abs field" style="left:271px;width:123px">Type Here :</div>
    <div class="abs btn search-btn">SEARCH</div>
  </form>
</section>

<main>
  <div class="abs tabs">
    <div class="tab active">FEATURED LISTING</div>
    <div class="tab">RECENT &nbsp;NEW</div>
    <div class="tab">ATEST LISTINGS</div>
  </div>
  <div class="abs listings">
    <article class="listing" style="top:0">
      <svg class="abs" style="left:0;top:18px" width="40" height="50" viewBox="0 0 40 50"><path d="M20 1a19 19 0 0 1 0 38a19 19 0 0 1 0-38z" fill="#222"/><path d="M1 20a19 19 0 0 1 38 0z" fill="#f7a51c"/><path d="M14 37l6 8l6-8z" fill="#222"/><text x="20" y="16" text-anchor="middle" font-size="11" font-weight="700" fill="#fff" font-family="Arimo,sans-serif">19</text><text x="20" y="32" text-anchor="middle" font-size="9" fill="#fff" font-family="Georgia,serif">Dec</text></svg>
      <h3 class="abs title">Neque porro quisquam dolorem ipsum</h3>
      <div class="abs meta"><span>📢 Published in <a>Photography</a></span><span>✎ Written by <a>Admin</a></span><span>💬 Comments <a>277</a></span></div>
      <div class="abs photo" role="img" aria-label="Photo of a group of friends looking at a tablet"></div>
      <h4 class="abs sub">NEQUE PORRO QUISQUAM</h4>
      <div class="abs stars">☆☆☆☆☆</div>
      <p class="abs body">Nam libero tempore, cum soluta nobis est eligendi optio cumque nihil impedit quo minus id quod maxime placeat facere possimus, omnis voluptas assumenda est, omnis dolor repellendu omnis dolor repellendus.....</p>
      <div class="abs btn more">Read More</div>
    </article>
    <div class="abs" style="left:0;top:186px;width:377px;border-top:1px solid var(--line)"></div>
    <article class="listing" style="top:179px">
      <svg class="abs" style="left:0;top:18px" width="40" height="50" viewBox="0 0 40 50"><path d="M20 1a19 19 0 0 1 0 38a19 19 0 0 1 0-38z" fill="#222"/><path d="M1 20a19 19 0 0 1 38 0z" fill="#f7a51c"/><path d="M14 37l6 8l6-8z" fill="#222"/><text x="20" y="16" text-anchor="middle" font-size="11" font-weight="700" fill="#fff" font-family="Arimo,sans-serif">19</text><text x="20" y="32" text-anchor="middle" font-size="9" fill="#fff" font-family="Georgia,serif">Dec</text></svg>
      <h3 class="abs title">Neque porro quisquam dolorem ipsum</h3>
      <div class="abs meta"><span>📢 Published in <a>Photography</a></span><span>✎ Written by <a>Admin</a></span><span>💬 Comments <a>277</a></span></div>
      <div class="abs photo" role="img" aria-label="Photo of a group of friends looking at a tablet"></div>
      <h4 class="abs sub">NEQUE PORRO QUISQUAM</h4>
      <div class="abs stars">☆☆☆☆☆</div>
      <p class="abs body">Nam libero tempore, cum soluta nobis est eligendi optio cumque nihil impedit quo minus id quod maxime placeat facere possimus, omnis voluptas assumenda est, omnis dolor repellendu omnis dolor repellendus.....</p>
      <div class="abs btn more">Read More</div>
    </article>
  </div>

  <aside>
    <h2 class="abs side-h" style="left:454px;top:421px"><span class="accent">QUILLVUE</span> FEEDS</h2>
    <div class="abs feed" style="top:450px"><div class="abs thumb" role="img" aria-label="Profile photo" style="background:linear-gradient(135deg,#c44,#e9c9a8,#46a)"></div><p>Aenean lacinia bibendum nulla sdgposuere @loremhandle nenatis dapfjkhkhglihlkilibus It is a pag <span class="hl">23 people recommeded This.....</span></p></div>
    <div class="abs feed" style="top:504px"><div class="abs thumb" role="img" aria-label="Profile photo" style="background:linear-gradient(135deg,#8cc4e6,#e6c38a,#b9d4ea)"></div><p>Aenean lacinia bibendum nulla sdgposuere @loremhandle nenatis dapfjkhkhglihlkilibus It is a pag <span class="hl">23 people recommeded This.....</span></p></div>
    <div class="abs feed" style="top:561px"><div class="abs thumb" role="img" aria-label="Profile photo" style="background:linear-gradient(135deg,#6a8a4a,#d8c0a0,#3a3a2a)"></div><p>Aenean lacinia bibendum nulla sdgposuere @loremhandle nenatis dapfjkhkhglihlkilibus It is a pag <span class="hl">23 people recommeded This.....</span></p></div>

    <h2 class="abs side-h" style="left:454px;top:615px"><span class="accent">CHIRPS</span> FEEDS</h2>
    <div class="abs tweet" style="top:641px"><span class="when">ABOUT 1 WEEK AGO</span>Aenean lacinia bib@lorempost.com osuere @loremhandle nenatis dapfjkhkhg ljhlhkilibus <span class="hl">23 that a reader will be distracted</span> by the readable content ...</div>
    <div class="abs tweet" style="top:692px"><span class="when">ABOUT 1 WEEK AGO</span>Aenean lacinia bib@lorempost.com osuere @loremhandle nenatis dapfjkhkhg ljhlhkilibus <span class="hl">23 that a reader will be distracted</span> by the readable content ...</div>
    <div class="abs tweet" style="top:744px"><span class="when">ABOUT 1 WEEK AGO</span>Aenean lacinia bib@lorempost.com osuere @loremhandle nenatis dapfjkhkhg ljhlhkilibus <span class="hl">23 that a reader will be distracted</span> by the readable content ...</div>
  </aside>

  <div class="abs divider"></div>
  <section class="intro">
    <h2 class="abs side-h intro-h"><span class="accent">INTRODUCTION</span> VIDEO</h2>
    <p style="top:858px">It is a long established fact that a reader will be distracted by the readable content of a page when looking at its layout. The point of using Lorem Ipsum is that it has a more-or-less normal distribution of letters, as opposed to using 'Content here, content here', making it look like readable English. Many desktop publishing packages and web page editors now use Lorem Ipsum as their default model text, and a search for 'lorem ipsum' will uncover many web sites still in their infancy</p>
    <p style="top:915px">Sed ut perspiciatis unde omnis iste natus error sit voluptatem accusantium doloremque laudantium, totam rem aperiam, eaque ipsa quae ab illo inventore veritatis et quasi architecto beatae vitae dicta sunt explicabo. Nemo enim ipsam voluptatem quia Neque porro quisquam est, qui dolorem ipsum quia dolor sit amet, consectetur, adipisci velit, sed quia non numquam eius modi tempora consequuntur magni dolores eos qui ratione voluptatem sequi nesciunt.</p>
    <div class="abs video" role="img" aria-label="Video still of a speaker on stage with a raised-hands audience and flags">
      <svg class="abs" style="left:88px;top:52px" width="24" height="24" viewBox="0 0 24 24"><circle cx="12" cy="12" r="11" fill="rgba(0,0,0,.35)"/><path d="M9 7l8 5l-8 5z" fill="#6fd34a"/></svg>
      <div class="abs bar">
        <div class="abs" style="left:0;top:0;width:200px;height:3px;background:#555"></div>
        <div class="abs" style="left:0;top:0;width:75px;height:3px;background:#d22"></div>
        <div class="abs" style="left:72px;top:-1px;width:5px;height:5px;border-radius:50%;background:#eee"></div>
        <svg class="abs" style="left:10px;top:6px" width="8" height="8"><path d="M1 1l6 3l-6 3z" fill="#ddd"/></svg>
        <span class="abs" style="left:48px;top:6px;font-size:5px;color:#ddd">0:03 / 0:15</span>
        <span class="abs" style="right:6px;top:5px;width:7px;height:6px;border:1px solid #ddd"></span>
      </div>
    </div>
  </section>
</main>

<footer class="abs footer">
  <h4 style="left:16px">ABOUT US</h4>
  <ul class="abs f-links"><li>Home</li><li>About Us</li><li>Featured</li><li>News</li><li>Reviews</li><li>Contact Us</li></ul>

  <h4 style="left:109px">LATEST NEWS</h4>
  <div class="abs news" style="top:36px"><b>Neque porro quisquam est qui dolorem</b><br>It is a long established fact that a reader<span class="day">25</span></div>
  <div class="abs news" style="top:70px"><b>Neque porro quisquam est qui dolorem</b><br>It is a long established fact that a reader<span class="day">25</span></div>
  <div class="abs news" style="top:106px"><b>Neque porro quisquam est qui dolorem</b><br>It is a long established fact that a reader<span class="day">25</span></div>

  <h4 style="left:273px">CONTACT US</h4>
  <div class="abs contact">Feel free to contact us if you have any problems.
    <ul><li>Address : Bldg. 190 lorem ipsum dummy</li><li>Email : hello@peerscope.test</li><li>Fax: (000)-121-1231</li><li>Phone : (000)-121-1231</li></ul>
  </div>

  <h4 style="left:428px">NEWSLETTER</h4>
  <div class="abs f-input" style="left:428px;top:36px">Name :</div>
  <div class="abs f-input" style="left:428px;top:66px">Email :</div>
  <div class="abs btn submit">SUBMIT</div>

  <div class="abs bottom">
    <span class="abs" style="left:13px;top:12px">© Copyright 2014 Peerscope. All Right Reserved.</span>
    <svg class="abs" style="left:454px;top:6px" width="106" height="20" viewBox="0 0 106 20" aria-hidden="true">
      <g fill="none" stroke="#ddd" stroke-width="1"><circle cx="10" cy="10" r="8.5"/><circle cx="31" cy="10" r="8.5"/><circle cx="52" cy="10" r="8.5"/><circle cx="73" cy="10" r="8.5"/><circle cx="95" cy="10" r="8.5"/></g>
    </svg>
  </div>
</footer>
</body>
</html>
```